BLENOX - Joining Study and Progress for Fair Opportunity

Brochure is needed for the European Project "BLENOX". We will distribute this flyer during conferences and events to our audiences (mainly academics, researchers, business individuals, policy makers and members of civil society groups) in order to provide the basic information about the project.
The main scope of the project is to support research organisations across Europe to design and implement gender equality plans in order to promote the women’s position of the filed of STEM research.

We are providing a video to explain the layout: https://www.vidstreamhub.example/watch?v=Xk4pR9tLm2Z.
We think size can range from A4-A3.

We are attaching files to provide with concrete information on our requirements:
- BLENOX Brochure Layout_SA.ppt: includes the content we would like to include in the flyer. There is also the URL to the project website
- blenox Logo.zip: the project logo
- Partners Logos.zip: the Logos that will be included
We would like to use colours that belong to the project logo colour range. Regarding the images that you may include in the flyer, we wouldn't like to propose any because we do not want to limitate your imagination. We have some at the website https://blenox-project.example/. They could be diverse (age, race, gender, etc.) relevant to women and men.

```html
<!DOCTYPE html>
<html lang="en">
<head>
<meta charset="utf-8">
<title>BLENOX Brochure</title>
<link rel="stylesheet" href="https://fonts.googleapis.com/css2?family=Mulish:wght@300;400;600;800;900&display=swap">
<style>
  :root {
    --backdrop: #e4e1dc;
    --paper: #f5f5f4;
    --paper-shade: #ececeb;
    --purple: #5050a2;
    --cover-yellow: #eec227;
    --inner-yellow: #e3b42a;
    --text-grey: #4a4a4a;
    --flag-blue: #1f47a8;
    --photo-a: #d9d6d2;
    --photo-b: #a4775a;
  }
  * { margin: 0; padding: 0; box-sizing: border-box; }
  html, body { width: 1200px; height: 1200px; overflow: hidden; }
  body {
    background: var(--backdrop);
    font-family: "Mulish", sans-serif;
    position: relative;
  }

  /* Cover */
  .cover {
    position: absolute; left: 124px; top: 235px;
    width: 456px; height: 644px;
    background: var(--paper);
    box-shadow: 0 6px 18px rgba(0,0,0,.18);
  }
  .brand {
    position: absolute; right: 25px; top: 58px;
    display: flex; align-items: center; gap: 8px;
  }
  .brand-dot {
    width: 22px; height: 22px; border-radius: 50%;
    background: var(--cover-yellow);
  }
  .brand-name {
    font-size: 25px; font-weight: 400; letter-spacing: 1px;
    color: var(--purple);
  }
  .cover-photo {
    position: absolute; left: 0; top: 149px;
    width: 430px; height: 306px;
    background: linear-gradient(110deg, var(--photo-a) 0%, #cfc9c3 45%, var(--photo-b) 100%);
  }
  .title-band {
    position: absolute; left: 122px; top: 359px;
    width: 334px; height: 132px;
    background: var(--cover-yellow);
    padding: 24px 28px 0 0;
    text-align: right;
    color: #fff;
    font-size: 19.5px; font-weight: 600; line-height: 20px;
    text-transform: uppercase;
  }
  .funding {
    position: absolute; left: 40px; top: 560px;
    display: flex; gap: 16px; align-items: flex-start;
  }
  .funding-badge { width: 65px; height: 43px; background: var(--flag-blue); }
  .funding-note {
    font-size: 9px; font-weight: 300; line-height: 11px;
    color: var(--text-grey); margin-top: 6px;
  }

  /* Inner spread */
  .inner-page {
    position: absolute; left: 656px; top: 235px;
    width: 462px; height: 650px;
    background: linear-gradient(90deg, var(--paper-shade) 0%, var(--paper) 8%, var(--paper) 92%, #e2e2e1 100%);
    box-shadow: 0 8px 22px rgba(0,0,0,.2);
  }
  .goal-heading {
    position: absolute; left: 92px; top: 182px;
    color: var(--purple); line-height: 1;
  }
  .goal-heading .small { display: block; font-size: 26px; font-weight: 800; }
  .goal-heading .large { display: block; font-size: 54px; font-weight: 900; letter-spacing: -1px; margin-top: -4px; }
  .goal-copy {
    position: absolute; left: 249px; top: 206px; width: 166px;
    font-size: 8.5px; line-height: 13px; font-weight: 400;
    color: var(--text-grey); text-align: justify;
    hyphens: manual;
  }
  .goal-copy p + p { margin-top: 11px; }
  .goal-block {
    position: absolute; left: 19px; top: 363px;
    width: 214px; height: 133px;
    background: var(--inner-yellow);
  }

  .next-page {
    position: absolute; left: 1121px; top: 237px;
    width: 90px; height: 646px;
    background: linear-gradient(90deg, #dcdcdb 0%, var(--paper) 20%);
    box-shadow: 0 8px 22px rgba(0,0,0,.18);
  }
  .partner-label {
    position: absolute; left: 51px;
    font-size: 15px; font-weight: 800; color: var(--purple);
    border-bottom: 2px solid var(--cover-yellow); line-height: 14px;
    white-space: nowrap;
  }
  .partner-mark { position: absolute; left: 51px; background: #2f2f4a; }
</style>
</head>
<body>

<section class="cover">
  <div class="brand">
    <span class="brand-dot"></span>
    <span class="brand-name">BLENOX</span>
  </div>
  <div class="cover-photo" role="img" aria-label="Photo of two smiling women talking in a bright office with a corkboard of sticky notes"></div>
  <h1 class="title-band">Joining<br>Study and Progress<br>for<br>Fair Opportunity</h1>
  <div class="funding">
    <div class="funding-badge"></div>
    <p class="funding-note">This project has received funding from the v's<br>Meridian 2020 Research and Innovation programme<br>under Grant Agreement&nbsp; No 904217</p>
  </div>
</section>

<section class="inner-page">
  <h2 class="goal-heading"><span class="small">the</span><span class="large">GOAL</span></h2>
  <div class="goal-copy">
    <p>BLENOX project supports 7 RPOs and 2 RFOs, that are in an initial stage, to develop Gender Equality Plans (GEPs) and engage the local Innovation Hubs to transfer the gained knowledge beyond academia.</p>
    <p>The project goal is to make research orga&shy;nizations more gender equal by increasing the number of female researchers in STEM, improving their careers prospects and inte&shy;grating a gender dimension in research.</p>
  </div>
  <div class="goal-block"></div>
</section>

<section class="next-page">
  <span class="partner-label" style="top:74px">PRO</span>
  <div class="partner-mark" style="top:118px;width:30px;height:18px"></div>
  <div class="partner-mark" style="top:180px;width:34px;height:34px;border-radius:50%;background:#bcbcbc"></div>
  <span class="partner-label" style="top:261px">RFO</span>
  <div class="partner-mark" style="top:302px;width:30px;height:30px;background:#2a2d5a"></div>
  <span class="partner-label" style="top:382px">SME</span>
  <div class="partner-mark" style="top:422px;width:24px;height:24px;border-radius:50%;background:#7f9cc8"></div>
  <span class="partner-label" style="top:495px">Pro</span>
  <div class="partner-mark" style="top:538px;width:36px;height:36px;border-radius:50%;background:#e2733f"></div>
</section>

</body>
</html>
```